Bussiness Oriented Flyer for an Outdoor Billboard Company

I'm looking for a front and back flyer design for my new company KEV Outdoor Media. We're an outdoor billboard company and you're welcome to check out the site to get a better idea of who we are. wwww.kevoutdoor.example

What I am looking for is for someone to design a flyer using all of the text from my PDF document which I have uploaded. The PDF is uploaded under "real estate media packet 2"

I would say I'm looking for a real clean and crisp look. This particular flyer is going to used in a more serious atmosphere and needs to have a real professional feel to it. I know it's a lot of text so it will limit the design but I'm hoping someone can design something that grabs the eye & feels professional.

I'm not looking for the document to not only be re-sized but rather redesigned. I am looking for someone to take the text from my document and create their own flyer. Try and have a theme of orange & dark grey because they're the company colors, I don't mind a little black but try to keep a theme of orange & dark grey. I am open to new layouts but it can't be overly flashy and the text must go in the same order.

MUST HAVES**

- Resemble the company's colors. Orange and Grey
- I am looking for a flyer size of 10"H x 6.5" Wide.
- Must be professional and business orientated. - Think "Pellow"
- The document has to have all of the text, and in the order that it is in, no text can be left out.
- Please remove the words from the two sketch drawings of the billboards.

Please email me if you have any questions at all
marcus@kevoutdoor.example

Reason: I am extending the deadline because I updated the text and added different pictures, please use download the new pictures and use them as seen in the PDF. Any questions please message me

```html
<!DOCTYPE html>
<html lang="en">
<head>
<meta charset="utf-8">
<title>KEV Outdoor Media – Flyer Front and Back</title>
<link rel="stylesheet" href="https://fonts.googleapis.com/css2?family=Gelasio:wght@700&family=Noto+Sans:ital,wght@0,400;0,700;1,400&display=swap">
<style>
  :root {
    --orange: #f15a1b;
    --orange-soft: #f58a4e;
    --slate: #8fa9bb;
    --ink: #161616;
    --paper: #ffffff;
    --backdrop: #e9e6e1;
  }
  * { box-sizing: border-box; margin: 0; padding: 0; }
  html, body { width: 1200px; height: 900px; overflow: hidden; }
  body { background: var(--backdrop); position: relative; font-family: "Noto Sans", Verdana, sans-serif; color: var(--ink); }

  .page { position: absolute; top: 48px; width: 516px; height: 794px; background: var(--paper); overflow: hidden; box-shadow: 0 4px 14px rgba(0,0,0,.18); }
  .page--front { left: 62px; }
  .page--back { left: 628px; width: 512px; }

  .brand { position: absolute; font-family: "Noto Sans", Verdana, sans-serif; font-weight: 700; color: var(--orange); font-size: 17px; line-height: 1; white-space: nowrap; }

  .front-art { position: absolute; inset: 0; }

  .headline { position: absolute; left: 31px; top: 90px; font-family: "Gelasio", Georgia, serif; font-weight: 700; font-size: 50px; line-height: 50px; letter-spacing: -0.5px; }

  .lede { position: absolute; left: 31px; top: 302px; width: 460px; }
  .section-title { color: var(--orange); font-weight: 700; font-size: 13px; line-height: 17px; }
  .lede p { font-size: 13.2px; line-height: 17.5px; }

  .col { position: absolute; }
  .col p { font-size: 11px; line-height: 14px; margin-top: 2px; }
  .col--costs { left: 31px; top: 441px; width: 200px; }
  .col--insured { left: 31px; top: 521px; width: 200px; }
  .col--payment { left: 265px; top: 441px; width: 215px; }

  .factors { list-style: none; margin-top: 12px; width: 180px; }
  .factors li { position: relative; padding-left: 31px; font-size: 11px; line-height: 14px; margin-bottom: 7px; }
  .factors li::before { content: ""; position: absolute; left: 4px; top: 2px; width: 11px; height: 10px; background: var(--orange); clip-path: polygon(25% 0, 75% 0, 100% 50%, 75% 100%, 25% 100%, 0 50%); }

  .site { position: absolute; left: 29px; bottom: 21px; color: var(--paper); font-style: italic; font-size: 13.5px; }

  .title-block { position: absolute; left: 31px; top: 96px; font-family: "Gelasio", Georgia, serif; font-weight: 700; line-height: 1; }
  .title-block .t1 { font-size: 26px; }
  .title-block .t2 { font-size: 32px; color: var(--orange); margin-top: 2px; }
  .title-block .t3 { font-size: 20px; margin-top: 4px; }

  .install { position: absolute; left: 204px; top: 30px; width: 280px; }
  .install h2 { font-size: 13px; font-weight: 700; margin-bottom: 2px; }
  .install p { font-size: 10.4px; line-height: 14px; letter-spacing: 0.15px; hyphens: auto; }

  .spec { position: absolute; left: 31px; width: 454px; border: 1px solid var(--orange-soft); }
  .spec--mono { top: 202px; height: 264px; }
  .spec--roof { top: 487px; height: 233px; }
  .spec__bar { display: flex; height: 28px; background: var(--slate); color: var(--paper); font-size: 10.5px; font-weight: 700; }
  .spec__bar span { flex: 1; text-align: center; line-height: 28px; }
  .spec__bar span.is-open { background: var(--paper); color: var(--slate); border-top: 4px solid var(--slate); line-height: 22px; }
  .spec__bar--split span { text-align: left; padding-left: 45px; }
  .spec__bar--split span:last-child { text-align: right; padding-right: 40px; }
  .spec__drawing { margin: 12px 18px 0; height: 110px; background: linear-gradient(180deg, #f6f7f8, #e9edf0); }
  .spec--roof .spec__drawing { height: 112px; }
  .spec h3 { color: var(--orange); font-size: 11.5px; font-weight: 700; margin: 14px 0 0 19px; }
  .spec p { font-size: 10.2px; line-height: 13.5px; margin: 1px 18px 0 19px; }

  .contact { position: absolute; left: 126px; top: 732px; display: flex; font-size: 11px; line-height: 14px; }
  .contact__who { text-align: right; padding-right: 12px; }
  .contact__who strong { display: block; font-size: 12px; }
  .contact__who em { font-style: italic; }
  .contact__rule { width: 8px; height: 44px; background: var(--orange); margin-right: 12px; }
  .contact__lines b { font-weight: 700; }
</style>
</head>
<body>

<section class="page page--front">
  <svg class="front-art" width="516" height="794" viewBox="0 0 516 794">
    <defs>
      <linearGradient id="sky" x1="0" y1="0" x2="0" y2="1">
        <stop offset="0" stop-color="#c9d9f0"/>
        <stop offset="0.45" stop-color="#c7a7e0"/>
        <stop offset="0.7" stop-color="#8a9ac0"/>
        <stop offset="1" stop-color="#c9a23a"/>
      </linearGradient>
    </defs>
    <circle cx="432" cy="140" r="158" fill="var(--orange)"/>
    <circle cx="446" cy="124" r="150" fill="url(#sky)" role="img" aria-label="Photo of a roadside billboard beside a highway at dusk"/>
    <path d="M0 718 C 120 690 260 700 370 728 C 440 746 490 730 516 704 L516 794 L0 794 Z" fill="var(--slate)"/>
    <path d="M516 600 C 500 660 470 700 420 720 C 300 760 150 700 0 736 L0 794 L516 794 Z" fill="var(--orange)"/>
    <path d="M0 736 C 150 700 300 760 420 720 C 470 700 500 660 516 600" fill="none" stroke="var(--paper)" stroke-width="3"/>
  </svg>

  <div class="brand" style="left:32px;top:44px;">KEV Outdoor Media</div>

  <h1 class="headline">Let your<br>property<br>work<br>for you!</h1>

  <div class="lede">
    <h2 class="section-title">Guaranteed long term income</h2>
    <p>With KEV Outdoor Media, your property will work for you. By leasing your commercial or industrial zoned property to us, we can provide you with a steady source of income.<br>All of our signs are virtually maintenance-free and can maximize a return on your property investments by increasing the potential re-sale value.</p>
  </div>

  <div class="col col--costs">
    <h2 class="section-title">No investments required</h2>
    <p>KEV Outdoor Media is responsible for ALL costs including installation, illumination, and maintenance.</p>
  </div>

  <div class="col col--insured">
    <h2 class="section-title">Fully Insured</h2>
    <p>KEV Outdoor Media holds you, the property owner, harmless from any claims or damages for bodily injuries and physical property damage caused by our sign structure or employees. We maintain liability insurance to cover all losses for which we may be responsible.</p>
  </div>

  <div class="col col--payment">
    <h2 class="section-title">The amount we will pay for leasing your property</h2>
    <p>These factors will determine the amount paid monthly to the property owner.</p>
    <ul class="factors">
      <li>Type of sign</li>
      <li>Traffic count</li>
      <li>Sign visibility</li>
      <li>Number of existing signs in the area</li>
      <li>Advertisers demand for coverage in the area</li>
    </ul>
  </div>

  <div class="site">www.kevoutdoor.example</div>
</section>

<section class="page page--back">
  <div class="brand" style="left:31px;top:44px;">KEV Outdoor Media</div>

  <div class="title-block">
    <div class="t1">Design and</div>
    <div class="t2">finishing</div>
    <div class="t3">specifications</div>
  </div>

  <div class="install" lang="en">
    <h2>Install</h2>
    <p>We will custom design each structure to both minimize ground space and ensure that there will be no inconvenience to any ongoing operations. We will ensure that the installation will cause as little disruption as possible.Our structures are safe and meet the most rigid engineering requirements. We are responsible for ensuring that our structures are fabricated and erected in compliance with local, state and federal regulations.</p>
  </div>

  <div class="spec spec--mono">
    <div class="spec__bar"><span>Center Mount</span><span>Flag Mount</span><span class="is-open">Top View</span></div>
    <div class="spec__drawing" role="img" aria-label="Line drawings of a monopole billboard: center mount, flag mount and top view"></div>
    <h3>Monopole</h3>
    <p>These billboards are constructed with a tubular steel support, tubular steel framing, and a double faced display panel. The foundation isOur structures are safe and meet the most rigid engineering requirements. We are responsible for ensuring that our structures are fabricated and erected in compliance with local, state and federal regulations.</p>
  </div>

  <div class="spec spec--roof">
    <div class="spec__bar spec__bar--split"><span>Side View</span><span>Front View</span></div>
    <div class="spec__drawing" role="img" aria-label="Line drawings of a roof mounted billboard: side view and front view"></div>
    <h3>Roof/ Fascia Mounted</h3>
    <p>These billboards are constructed with angle iron, steel supports and metal framing. The steel supports are mounted to the roof using fascia mounting brackets. Each billboard is a single faced display and varies in size depending on your custom design.</p>
  </div>

  <div class="contact">
    <div class="contact__who"><strong>Contact</strong><em>Dana Morrow</em></div>
    <div class="contact__rule"></div>
    <div class="contact__lines">
      <div><b>Web.</b> kevoutdoor.example</div>
      <div><b>Tel.</b> (555) 014 – 2731</div>
      <div><b>E-mail.</b> marcus@kevoutdoor.example</div>
    </div>
  </div>
</section>

</body>
</html>
```